Hypnotherapy- past life regression-life between lives therapist needs a website

I need a website that is enticing and spiritual in its feeling. It needs to have a lot of beautiful nature pictures included. The theme is "Quiet Harbor Path- what might you find....Lessons Solutions Answers"
Because all of us have the answers to living our best life, they are in our subconcious. But not everyone is capable of accessing them. Hypnosis accesses the subconcious and helps to create new neural pathways in the brain which can create new behaviors and responses to situations.
Hypnosis can help with anxiety, pain relief, weight loss, smoking/vaping cessation, self confidence......anything about yourself that you want to change.
Exploration of past lives and life between lives can reveal things related to ones current life. For example, perhaps your fear of deep water is a result of drowning in a past life. Once this has been discovered, it can lead to changes in ones current life.
Almost any personal behavior one wants to change, can be helped through hypnotherapy.
I need a page for testimonials, a place for scheduling (I will have a link to my scheduling app) some information about hypnotherapy.
I am uploading my logo files. My business card will be using the black and gold style, but my website does not have to reflect that. It can be based on the caramel and deep green like full color logo. Earthy, calm colors.
I also like the mock up of my logo on the beach and there was one on a starry night sky that I also liked.
Target Market(s)
men and women ages 25-50
Industry/Entity Type
natural health and wellness, spirituality
Number of Pages Required
4 page
Requirements
Must have
- a page for testimonials, perhaps with a beautiful nature picture with each one, I will have approximately 6. A link to schedule a complimentary intro session, preferably on the first page
Should not have
- no swinging watches or other sterotyped hypnosis symbols

```html
<!DOCTYPE html>
<html lang="en">
<head>
<meta charset="utf-8">
<title>Quiet Harbor Path – Hypnotherapy</title>
<link href="https://fonts.googleapis.com/css2?family=Open+Sans:wght@400;600;700&family=Gelasio:wght@400;700&display=swap" rel="stylesheet">
<style>
:root{
  --olive:#5c5a2e;
  --orange:#e08a2c;
  --lavender:#f1eff8;
  --panel:#eeecf7;
  --ink:#2d2d2d;
  --grey:#8a8a8a;
  --dark:#2b2e36;
  --navy:#313b5a;
  --white:#ffffff;
}
*{margin:0;padding:0;box-sizing:border-box}
html,body{width:1200px;height:4517px;overflow:hidden}
body{position:relative;background:var(--white);font-family:"Open Sans",sans-serif;color:var(--ink)}
.abs{position:absolute}
.serif{font-family:"Gelasio",serif}
.center{text-align:center;left:0;width:1200px}

/* header */
.icon-dot{position:absolute;width:28px;height:28px;border-radius:50%;background:var(--olive)}
.contact-label{position:absolute;font-size:11px;font-weight:700;line-height:13px}
.contact-label span{display:block;font-weight:400;color:var(--grey);font-size:10px}
.nav a{position:absolute;top:87px;font-size:12px;font-weight:600;color:var(--ink);text-decoration:none}
.brand{position:absolute;display:flex;flex-direction:column;align-items:center;gap:4px;font-family:"Gelasio",serif;color:var(--orange);font-size:13px;font-weight:700;letter-spacing:1px}
.brand i{display:block;border:2px solid var(--orange);border-radius:50%}
.btn{position:absolute;display:flex;align-items:center;justify-content:center;border-radius:26px;font-size:13px;font-weight:700;text-transform:uppercase}

/* hero */
.hero{position:absolute;top:123px;left:0;width:1200px;height:780px;background:linear-gradient(100deg,#2a2218 0%,#4a3a26 40%,#6b5536 62%,#3a2e20 100%)}
.hero-eyebrow{top:362px;left:81px;font-size:24px;letter-spacing:3px;color:#fff;font-weight:600}
.hero-title{top:410px;left:80px;font-size:50px;font-weight:700;color:#fff}
.hero-rule{top:494px;left:81px;width:600px;height:2px;background:#fff}
.hero-copy{top:527px;left:82px;width:620px;font-size:15px;line-height:27px;color:#fff;font-weight:600}

/* about */
.about-photo{left:94px;top:969px;width:448px;height:448px;border-radius:50%;background:radial-gradient(circle at 40% 35%,#d9c4a4,#9c7a4f 45%,#4e3b25 100%)}
.eyebrow{font-size:17px;color:var(--olive)}
.h2{color:var(--olive);font-family:"Gelasio",serif;font-weight:400}
.quote-box{left:621px;top:1130px;width:460px;height:62px;border-left:2px solid #999;padding:8px 0 0 15px;font-size:12.5px;line-height:22px;color:var(--grey)}
.para{font-size:12.5px;line-height:23px;color:var(--grey)}

/* services */
.band{position:absolute;left:0;width:1200px;background:var(--lavender)}
.service{position:absolute;top:1749px;width:320px;height:269px;border-radius:6px;padding:56px 0 0 20px;color:#fff;font-family:"Gelasio",serif;font-weight:700;font-size:27px}
.badge{position:absolute;width:74px;height:74px;border-radius:50%;background:#fff;top:1712px;display:flex;align-items:center;justify-content:center;box-shadow:0 2px 8px rgba(0,0,0,.12)}

/* why */
.why-title{font-size:20px;color:var(--olive);font-family:"Gelasio",serif}
.why-copy{font-size:12.5px;line-height:23px;color:var(--grey);margin-top:6px}
.why-left{text-align:right;width:300px;left:74px}
.why-right{width:300px;left:796px}
.ring{position:absolute;width:96px;height:96px;border-radius:50%;background:#fff;border:2px solid #efe3d6;display:flex;align-items:center;justify-content:center}
.ring b{width:80px;height:80px;border-radius:50%;background:var(--olive);display:flex;align-items:center;justify-content:center}

/* hours */
.hours{top:2816px;height:561px;left:0;width:1200px;background:linear-gradient(110deg,#1d1a17 0%,#3a3128 45%,#2c241d 70%,#15110e 100%)}
.row{position:absolute;left:133px;width:418px;display:flex;justify-content:space-between;font-size:15px;color:#fff;font-weight:700}
.row span:last-child{font-weight:400;color:#9a948c;font-size:14px}
.sep{position:absolute;left:123px;width:465px;height:1px;background:rgba(255,255,255,.18)}
.field{position:absolute;background:#fff;height:53px;font-size:13px;color:#777;padding:19px 0 0 26px}

/* reviews */
.review{position:absolute;top:3651px;width:321px;height:267px;background:#fff;border-radius:6px;box-shadow:0 4px 18px rgba(0,0,0,.05);padding:56px 26px 0 26px}
.avatar{position:absolute;top:-32px;left:26px;width:66px;height:66px;border-radius:50%;background:linear-gradient(160deg,#d8d2c8,#8d8377);border:4px solid #fff}
.qmark{position:absolute;top:-20px;right:36px;font-family:"Gelasio",serif;font-size:90px;line-height:90px;color:#dcdcdc}
.stars{color:var(--orange);font-size:15px;letter-spacing:3px}
.review p{font-size:12.5px;line-height:23px;color:var(--grey);margin-top:8px}
.reviewer{font-family:"Gelasio",serif;color:var(--olive);font-size:19px;margin-top:10px}
.role{font-size:9px;color:var(--grey);letter-spacing:.5px}

/* footer */
.footer{top:3990px;height:475px;left:0;width:1200px;background:var(--dark)}
.fnav a{position:absolute;top:4282px;font-size:13px;font-weight:700;color:#fff;text-decoration:none;transform:translateX(-50%)}
.fcircle{position:absolute;width:56px;height:56px;border-radius:50%;border:1.5px solid #fff;display:flex;align-items:center;justify-content:center}
.finfo{position:absolute;font-size:12px;color:#fff;font-weight:700;line-height:19px}
.finfo span{font-weight:600;font-size:11px;display:block}
.bar{top:4465px;height:52px;left:0;width:1200px;background:var(--navy)}
.social{position:absolute;top:4480px;width:25px;height:25px;border:1.5px solid #fff;border-radius:3px}
</style>
</head>
<body>

<!-- header -->
<div class="icon-dot" style="left:123px;top:19px"></div>
<svg class="abs" style="left:130px;top:26px" width="14" height="14" viewBox="0 0 24 24"><path d="M6.6 10.8a15 15 0 006.6 6.6l2.2-2.2c.3-.3.7-.4 1-.2 1.1.4 2.3.6 3.6.6.6 0 1 .4 1 1V20c0 .6-.4 1-1 1A17 17 0 013 4c0-.6.4-1 1-1h3.5c.6 0 1 .4 1 1 0 1.3.2 2.5.6 3.6.1.3 0 .7-.2 1z" fill="#fff"/></svg>
<div class="contact-label" style="left:161px;top:20px">Call Us:<span>(555) 014 2286</span></div>
<div class="icon-dot" style="left:281px;top:19px"></div>
<svg class="abs" style="left:288px;top:27px" width="14" height="12" viewBox="0 0 24 20"><rect x="1" y="1" width="22" height="18" rx="2" fill="none" stroke="#fff" stroke-width="2.5"/><path d="M1 3l11 8 11-8" fill="none" stroke="#fff" stroke-width="2.5"/></svg>
<div class="contact-label" style="left:319px;top:20px">Email:<span>office@company.com</span></div>
<div class="abs" style="left:123px;top:69px;width:360px;height:1px;background:#ccc"></div>
<nav class="nav">
  <a style="left:123px">Home</a><a style="left:237px">About Us</a><a style="left:386px">Services</a>
  <a style="left:705px">Team</a><a style="left:833px">Blog</a><a style="left:956px">Contact Us</a>
</nav>
<div class="brand" style="left:500px;top:16px;width:150px"><i style="width:50px;height:50px"></i>QUIET HARBOR PATH</div>
<div class="btn" style="left:879px;top:12px;width:184px;height:39px;background:var(--olive);color:#fff;font-size:11.5px">Book Appointment</div>

<!-- hero -->
<div class="hero" role="img" aria-label="Woman standing in a golden meadow at sunset"></div>
<div class="abs hero-eyebrow">HYPNOTHERAPY SERVICES</div>
<h1 class="abs hero-title">Transcendent Hypnosis</h1>
<div class="abs hero-rule"></div>
<p class="abs hero-copy">Lorem ipsum dolor sit amet, consectetur adipiscing elit et dolore conser tempor incididunt ut labore et dolore magna</p>
<div class="btn" style="left:82px;top:612px;width:146px;height:39px;background:var(--orange);color:#fff">Learn More</div>
<div class="btn" style="left:240px;top:612px;width:179px;height:39px;background:#fff;color:var(--ink)">Request Quote</div>
<svg class="abs" style="left:0;top:760px" width="1200" height="160"><path d="M0 30 Q600 204 1200 30 L1200 160 L0 160Z" fill="#fff"/><path d="M237 100 Q600 160 961 100" fill="none" stroke="var(--orange)" stroke-width="4"/></svg>
<div class="abs" style="left:570px;top:860px;width:60px;height:60px;border-radius:50%;background:#fff;border:2px solid var(--orange)"></div>

<!-- about -->
<svg class="abs" style="left:81px;top:956px" width="474" height="474"><path d="M12 260 A225 225 0 1 1 230 461" fill="none" stroke="var(--orange)" stroke-width="8"/></svg>
<div class="abs about-photo" role="img" aria-label="Woman breathing in autumn forest air"></div>
<div class="abs eyebrow serif" style="left:621px;top:978px">Strength in Hypnotherapy</div>
<h2 class="abs h2" style="left:620px;top:1006px;font-size:42px;line-height:54px">Cultivate Wellness,<br>Elevate Consciousness</h2>
<div class="abs quote-box">Lorem ipsum dolor sit amet, consectetur adipiscing elit, sed do eiusmod<br>or incididunt ut labore et dolore</div>
<p class="abs para" style="left:621px;top:1214px;width:470px">Lorem ipsum dolor sit amet, consectetur adipiscing elit, sed do eiusmod tem por incididunt ut labore et dolore magna aliqua. Ut enim ad minim veniam, quis nostrud exercitation ullamco laboris nisi ut aliquip ex ea commodo consequat. Duis aute irure dolor in reprehenderit in voluptate velit esse cillum dolore eu fugiat nulla pariatur. Excepteur</p>
<div class="abs" style="left:619px;top:1361px;width:155px;height:46px;background:var(--orange);border-radius:3px;color:#fff;font-size:14px;font-weight:700;display:flex;align-items:center;gap:16px;padding-left:16px">Contact us
<svg width="18" height="14" viewBox="0 0 18 14"><path d="M1 7h15M10 1l6 6-6 6" fill="none" stroke="#fff" stroke-width="2"/></svg></div>

<!-- services -->
<section class="band" style="top:1512px;height:572px"></section>
<h2 class="abs h2 center" style="top:1563px;font-size:44px">Our Services</h2>
<p class="abs para center" style="top:1628px">Lorem ipsum dolor sit amet, consectetur adipiscing elit, sed do eiusmod temp<br>or incididunt ut labore et dolore</p>
<div class="service" style="left:91px;background:linear-gradient(160deg,#7d6a55,#3d4a3a)" role="img" aria-label="Therapist listening to a client">Emotional Healing</div>
<div class="service" style="left:439px;background:linear-gradient(160deg,#8a7b68,#4a3c2e)" role="img" aria-label="Woman smiling in warm light">Past Life Regression</div>
<div class="service" style="left:786px;background:linear-gradient(160deg,#6e4a3c,#aab0b8)" role="img" aria-label="Client relaxing on a couch">Phobia Resolution</div>
<div class="badge" style="left:134px"><svg width="30" height="30" viewBox="0 0 24 24"><circle cx="16" cy="5" r="2.5" fill="var(--orange)"/><path d="M13 22v-8l3-3 3 3v8M3 22v-5M7 22v-8M10 22v-11" stroke="var(--orange)" stroke-width="2" fill="none"/></svg></div>
<div class="badge" style="left:481px"><svg width="28" height="28" viewBox="0 0 24 24"><circle cx="12" cy="12" r="9" fill="none" stroke="var(--orange)" stroke-width="1.5"/><circle cx="12" cy="12" r="5" fill="none" stroke="var(--orange)" stroke-width="2"/><circle cx="12" cy="12" r="1.8" fill="var(--orange)"/></svg></div>
<div class="badge" style="left:828px"><svg width="30" height="30" viewBox="0 0 24 24"><path d="M9 21v-9a2 2 0 014 0v4l4 1v4M9 16l-2-2" fill="none" stroke="var(--orange)" stroke-width="2"/><circle cx="11" cy="6" r="4" fill="none" stroke="var(--orange)" stroke-width="1.5"/></svg></div>

<!-- why choose us -->
<h2 class="abs h2 center" style="top:2138px;font-size:44px">Why Choose Us</h2>
<p class="abs para center" style="top:2204px">Lorem ipsum dolor sit amet, consectetur adipiscing elit, sed do eiusmod temp<br>or incididunt ut labore et dolore</p>
<div class="abs" style="left:395px;top:2320px;width:200px;height:430px;border-radius:215px 0 0 215px;background:linear-gradient(90deg,#fff,#ebe8f5)"></div>
<div class="abs" style="left:605px;top:2320px;width:200px;height:430px;border-radius:0 215px 215px 0;background:linear-gradient(270deg,#fff,#ebe8f5)"></div>
<div class="abs" style="left:418px;top:2330px;width:364px;height:364px;border-radius:50%;background:radial-gradient(circle at 50% 40%,#9aa0b5,#3e4a78 70%)" role="img" aria-label="Smiling therapist with arms crossed"></div>

<div class="abs why-left" style="top:2360px"><div class="why-title">Quality Assurance</div><div class="why-copy">Lorem ipsum dolor sit amet, consectet<br>ur adipiscing elit et dolore conser</div></div>
<div class="abs why-left" style="top:2492px"><div class="why-title">Client-centric</div><div class="why-copy">Lorem ipsum dolor sit amet, consectet<br>ur adipiscing elit et dolore conser</div></div>
<div class="abs why-left" style="top:2624px"><div class="why-title">Proven Results</div><div class="why-copy">Lorem ipsum dolor sit amet, consectet<br>ur adipiscing elit et dolore conser</div></div>
<div class="abs why-right" style="top:2360px"><div class="why-title">Expertise and Experience</div><div class="why-copy">Lorem ipsum dolor sit amet, consectet<br>ur adipiscing elit et dolore conser</div></div>
<div class="abs why-right" style="top:2492px"><div class="why-title">Personalized Approach</div><div class="why-copy">Lorem ipsum dolor sit amet, consectet<br>ur adipiscing elit et dolore conser</div></div>
<div class="abs why-right" style="top:2624px"><div class="why-title">Innovative</div><div class="why-copy">Lorem ipsum dolor sit amet, consectet<br>ur adipiscing elit et dolore conser</div></div>

<div class="ring" style="left:392px;top:2352px"><b><svg width="34" height="34" viewBox="0 0 24 24"><circle cx="12" cy="4" r="2" fill="#fff"/><path d="M4 8h16M12 8v6l-4 7M12 14l4 7" stroke="#fff" stroke-width="2" fill="none"/></svg></b></div>
<div class="ring" style="left:392px;top:2484px"><b><svg width="34" height="34" viewBox="0 0 24 24"><g stroke="#fff" stroke-width="2.2" stroke-linecap="round"><path d="M12 3v3M12 18v3M3 12h3M18 12h3M5.6 5.6l2.1 2.1M16.3 16.3l2.1 2.1M5.6 18.4l2.1-2.1M16.3 7.7l2.1-2.1"/></g></svg></b></div>
<div class="ring" style="left:392px;top:2616px"><b><svg width="34" height="34" viewBox="0 0 24 24"><path d="M5 14a7 7 0 0114 0v3H5zM3 17h18M9 21h6" fill="none" stroke="#fff" stroke-width="2"/></svg></b></div>
<div class="ring" style="left:685px;top:2352px"><b><svg width="34" height="34" viewBox="0 0 24 24"><circle cx="12" cy="12" r="9" fill="none" stroke="#fff" stroke-width="1.5" stroke-dasharray="2 2"/><circle cx="12" cy="12" r="5" fill="none" stroke="#fff" stroke-width="2"/><circle cx="12" cy="12" r="2" fill="#fff"/></svg></b></div>
<div class="ring" style="left:685px;top:2484px"><b><svg width="34" height="34" viewBox="0 0 24 24"><path d="M5 14a7 7 0 0114 0v3H5zM3 17h18M9 21h6" fill="none" stroke="#fff" stroke-width="2"/></svg></b></div>
<div class="ring" style="left:685px;top:2616px"><b><svg width="34" height="34" viewBox="0 0 24 24"><rect x="3" y="3" width="6" height="6" fill="none" stroke="#fff" stroke-width="2"/><rect x="15" y="15" width="6" height="6" fill="none" stroke="#fff" stroke-width="2"/><path d="M9 6h9v9M6 9v9h9" fill="none" stroke="#fff" stroke-width="2"/></svg></b></div>

<!-- opening hours & appointment -->
<section class="abs hours" role="img" aria-label="Silhouette on a misty hillside at dusk"></section>
<h3 class="abs serif" style="left:93px;top:2948px;font-size:28px;font-weight:400;color:#fff">Opening Hours</h3>
<div class="abs" style="left:96px;top:3014px;width:3px;height:232px;background:var(--orange)"></div>
<div class="row" style="top:3043px"><span>Monday - Friday</span><span>08am - 05pm</span></div>
<div class="sep" style="top:3079px"></div>
<div class="row" style="top:3094px"><span>Saturday</span><span>08am - 05pm</span></div>
<div class="sep" style="top:3129px"></div>
<div class="row" style="top:3144px"><span>Telephone</span><span>+123 456 7890</span></div>
<div class="sep" style="top:3180px"></div>
<div class="row" style="top:3195px"><span>Email</span><span>info@company.com</span></div>

<div class="abs" style="left:612px;top:2842px;width:491px;height:500px;background:var(--panel)"></div>
<div class="abs" style="left:665px;top:2881px;width:56px;height:56px;border-radius:50%;background:var(--olive);display:flex;align-items:center;justify-content:center"><svg width="26" height="22" viewBox="0 0 24 20"><rect x="1" y="3" width="22" height="16" rx="1" fill="none" stroke="#ddd" stroke-width="1.6"/><path d="M1 4l11 8 11-8M5 1h14" fill="none" stroke="#ddd" stroke-width="1.6"/></svg></div>
<div class="abs" style="left:733px;top:2880px;font-size:13px;color:var(--ink)">Get in touch with us for more information</div>
<h3 class="abs h2" style="left:733px;top:2902px;font-size:32px">Make Appointment</h3>
<div class="field" style="left:667px;top:2977px;width:182px">First Name</div>
<div class="field" style="left:867px;top:2977px;width:184px">Last Name</div>
<div class="field" style="left:667px;top:3049px;width:182px">Email Address</div>
<div class="field" style="left:867px;top:3049px;width:184px">Phone Number</div>
<div class="field" style="left:667px;top:3122px;width:384px">Select Subject</div>
<div class="field" style="left:667px;top:3194px;width:384px">dd/mm/yyyy</div>
<div class="abs" style="left:667px;top:3267px;width:384px;height:52px;background:var(--orange);color:#fff;font-size:17px;font-weight:700;display:flex;align-items:center;justify-content:center">SUBMIT</div>

<!-- reviews -->
<section class="band" style="top:3377px;height:640px"></section>
<h2 class="abs h2 center" style="top:3456px;font-size:44px">Client Reviews</h2>
<p class="abs para center" style="top:3522px">Lorem ipsum dolor sit amet, consectetur adipiscing elit, sed do eiusmod temp<br>or incididunt ut labore et dolore</p>

<div class="review" style="left:102px"><div class="avatar" role="img" aria-label="Client portrait"></div><div class="qmark">”</div><div class="stars">★★★★★</div><p>Lorem ipsum dolor sit amet, consectetur adipiscing elit, sed do eiusmod tempor inci didunt ut labore et dolore magna aliqua. Ut enim ad minim veniam, quis</p><div class="reviewer">Mara Elwood</div><div class="role">BUSINESSMAN</div></div>
<div class="review" style="left:446px;border-bottom:4px solid var(--orange)"><div class="avatar" role="img" aria-label="Client portrait"></div><div class="qmark" style="color:var(--olive)">”</div><div class="stars">★★★★★</div><p>Lorem ipsum dolor sit amet, consectetur adipiscing elit, sed do eiusmod tempor inci didunt ut labore et dolore magna aliqua. Ut enim ad minim veniam, quis</p><div class="reviewer">Mara Elwood</div><div class="role">BUSINESSMAN</div></div>
<div class="review" style="left:788px"><div class="avatar" role="img" aria-label="Client portrait"></div><div class="qmark">”</div><div class="stars">★★★★★</div><p>Lorem ipsum dolor sit amet, consectetur adipiscing elit, sed do eiusmod tempor inci didunt ut labore et dolore magna aliqua. Ut enim ad minim veniam, quis</p><div class="reviewer">Mara Elwood</div><div class="role">BUSINESSMAN</div></div>

<!-- footer -->
<footer class="abs footer"></footer>
<svg class="abs" style="left:0;top:3988px" width="1200" height="110"><path d="M0 0 L1200 0 L1200 2 Q600 132 0 2Z" fill="var(--lavender)"/><path d="M237 56 Q600 110 961 56" fill="none" stroke="var(--orange)" stroke-width="4"/></svg>
<div class="abs" style="left:572px;top:4043px;width:56px;height:56px;border-radius:50%;background:#fff;border:2px solid var(--orange)"></div>
<div class="brand" style="left:500px;top:4166px;width:200px"><i style="width:52px;height:52px"></i>QUIET HARBOR PATH</div>
<nav class="fnav"><a style="left:380px">HOME</a><a style="left:482px">SERVICES</a><a style="left:592px">ABOUT US</a><a style="left:726px">TESTIMONIALS</a><a style="left:846px">BLOG</a></nav>
<div class="abs" style="left:140px;top:4332px;width:920px;height:1px;background:rgba(255,255,255,.4)"></div>

<div class="fcircle" style="left:172px;top:4377px"><svg width="30" height="30" viewBox="0 0 24 24"><circle cx="12" cy="12" r="9" fill="none" stroke="#fff" stroke-width="1.5"/><path d="M3 12h18M12 3c3 3 3 15 0 18M12 3c-3 3-3 15 0 18" fill="none" stroke="#fff" stroke-width="1.5"/></svg></div>
<div class="finfo" style="left:247px;top:4386px;font-size:11px">123, Building Name, Street<br>City, State XY 123456</div>
<div class="abs" style="left:430px;top:4375px;width:1px;height:60px;background:rgba(255,255,255,.4)"></div>
<div class="fcircle" style="left:507px;top:4377px"><svg width="22" height="28" viewBox="0 0 16 24"><rect x="2" y="1" width="12" height="22" rx="2" fill="none" stroke="#fff" stroke-width="1.6"/><circle cx="8" cy="19" r="1.2" fill="#fff"/></svg></div>
<div class="finfo" style="left:579px;top:4384px">PHONE<span>(123) 456 7890</span></div>
<div class="abs" style="left:749px;top:4375px;width:1px;height:60px;background:rgba(255,255,255,.4)"></div>
<div class="fcircle" style="left:828px;top:4377px"><svg width="28" height="24" viewBox="0 0 24 20"><rect x="1" y="3" width="22" height="16" rx="1" fill="none" stroke="#fff" stroke-width="1.5"/><path d="M1 4l11 8 11-8" fill="none" stroke="#fff" stroke-width="1.5"/></svg></div>
<div class="finfo" style="left:903px;top:4384px">EMAIL<span>info@company.com</span></div>

<div class="abs bar"></div>
<div class="abs serif" style="left:153px;top:4482px;font-size:13px;color:#fff">Quiet Harbor Path</div>
<div class="social" style="left:933px"></div>
<div class="social" style="left:966px"></div>
<div class="social" style="left:999px"></div>
<div class="social" style="left:1032px"></div>

</body>
</html>
```